Drug safety monitoring company requires a new corporate website

We are an outsourcing partner to large and small companies within the pharmaceutical industry. Our current website www.quorvanta.co.uk has not been updated in a long time. We want a new web site that is responsive and modern but with a clearly corporate and professional feel. We want a design based on a 12 column grid system (mobile and desktop version). We want to use a new, modern font (not the standard web fonts) - we will purchase as required. Content can be used as is from the current website. Red and white are the corporate colours, so a palate should be developed to match. We do not need as much red as is in the current website. New icons (preferably in svg format) would be great. We can also purchase new images from Framly (or other) as required. We would prefer submissions in Sketch if possible.

Target Market(s)

Pharmaceutical companies

Number of Pages Required

1 page

Font styles to use
Sans Serif

Colors
ec1f27
ffffff

Requirements
Must have
• Design based on 12 column grid system.
Responsive design (i.e. require a mobile and desktop version).
How should the menu look between desktop and mobile?
A coherent colour palete.
Content to come from the existing website: www.quorvanta.co.uk
How should links be styled?
How should headings, sub-headings, paragraphs be styled?
Nice to have
• Custom developed icons (these are along the bottom of the page on the existing website: Medical Information; Pharmacovigilance; Literature Monitoring; Training).
New imagery (the images on the current website are dated).
Submission ideally as Sketch files (but we are okay with photoshop too).
A new, modern, non-standard font.
Not so much red in the design.
If we had buttons on the website, how should they be styled?
If we had a form on the website, how should the fields be styled?

```html
<!DOCTYPE html>
<html lang="en">
<head>
<meta charset="utf-8">
<title>Quorvanta Pharmacovigilance</title>
<link href="https://fonts.googleapis.com/css2?family=Ubuntu:wght@400;500;700&display=swap" rel="stylesheet">
<style>
:root{
  --red:#ec1f27;
  --white:#ffffff;
  --hero:#3d3878;
  --navy:#1c1567;
  --ink:#2f2f2f;
  --body:#3a3a3a;
}
*{margin:0;padding:0;box-sizing:border-box}
html,body{width:1200px;height:2598px;overflow:hidden}
body{position:relative;font-family:'Ubuntu',sans-serif;background:var(--white);color:var(--body)}
.abs{position:absolute}
.hero{left:0;top:0;width:1200px;height:682px;background:var(--hero);overflow:hidden}
.hero-visual{position:absolute;left:600px;top:90px;width:520px;height:520px;border-radius:50%;
  background:radial-gradient(circle at 60% 45%,rgba(90,90,170,.55),rgba(61,56,120,0) 70%)}
.brand{display:flex;align-items:center;gap:10px;color:var(--white);font-weight:500;font-size:24px;white-space:nowrap}
.brand-mark{width:14px;height:14px;background:var(--red)}
.menu{left:1009px;top:42px;width:43px}
.menu span{display:block;height:4px;background:var(--red);border-radius:2px;margin-bottom:10px}
.hero-title{left:280px;width:640px;top:218px;text-align:center;color:var(--white);font-weight:700;font-size:38px;line-height:51px}
.btn{display:inline-flex;align-items:center;justify-content:center;background:var(--red);color:var(--white);
  font-weight:700;border-radius:27px;text-decoration:none}
.hero-btn{left:503px;top:467px;width:191px;height:54px;font-size:19px}
.learn{left:0;width:1200px;top:533px;text-align:center}
.learn a{color:var(--white);font-weight:700;font-size:18px;text-decoration:underline}
.scroll{left:578px;top:611px;width:43px;height:43px;border-radius:50%;background:var(--white);display:flex;align-items:center;justify-content:center}
.section-title{left:0;width:1200px;text-align:center;color:var(--ink);font-weight:700;font-size:39px}
.info{width:395px}
.info h3{font-size:18.5px;font-weight:500;color:var(--ink);line-height:26px;margin-bottom:14px;letter-spacing:.3px}
.info p{font-size:17.5px;line-height:25.6px;letter-spacing:.4px}
.info a{color:var(--red);text-decoration:none;font-size:17.5px;line-height:25.6px;letter-spacing:.4px}
.card{width:281px;height:310px;background:var(--white);box-shadow:0 2px 10px rgba(0,0,0,.1);text-align:center;padding-top:12px}
.card svg{display:block;margin:0 auto}
.card h4{color:var(--red);font-weight:500;font-size:19.5px;margin-top:6px;letter-spacing:.4px}
.card p{font-size:16px;line-height:20.5px;margin:34px auto 0;width:210px;letter-spacing:.3px}
.card .btn{position:absolute;left:47px;bottom:14px;width:189px;height:53px;font-size:19px}
.footer{left:0;top:2189px;width:1200px;height:409px;background:var(--navy);color:var(--white)}
.footer h2{position:absolute;font-weight:700;font-size:40px}
.footer p{position:absolute;font-size:18px;font-weight:500}
.social{position:absolute;left:207px;top:224px;display:flex;gap:12px}
.social span{width:32px;height:32px;border-radius:50%;background:var(--red)}
.copy{left:508px;top:339px;font-size:18px;line-height:23px;font-weight:500}
</style>
</head>
<body>

<header class="abs hero">
  <div class="hero-visual" role="img" aria-label="Close-up photograph of coloured capsules in a glass dish"></div>
  <div class="abs brand" style="left:148px;top:46px"><span class="brand-mark"></span>Quorvanta</div>
  <div class="abs menu"><span></span><span></span><span></span></div>
  <h1 class="abs hero-title">At Quorvanta we ansure that your business has the best Pharmacovigilance support in the industry</h1>
  <a class="abs btn hero-btn" href="#">Get Started Now</a>
  <div class="abs learn"><a href="#">Learn more</a></div>
  <div class="abs scroll"><svg width="16" height="10" viewBox="0 0 16 10"><path d="M2 2l6 6 6-6" fill="none" stroke="#ec1f27" stroke-width="2.2" stroke-linecap="round"/></svg></div>
</header>

<h2 class="abs section-title" style="top:764px">Welcome</h2>

<div class="abs info" style="left:148px;top:888px">
  <h3>Welcome to the Quorvanta<br>Pharmacovigilance</h3>
  <p>We are an outsourcing partner to large and small companies within the pharmaceutical industry Our range of services is tailored to suit each of our client’s needs and cover both human and veterinary</p>
  <a href="#">Read more...</a>
</div>
<div class="abs info" style="left:659px;top:913px">
  <h3>Pharmacovigilance</h3>
  <p>is defined by WHO as ‘The science and activities relating to the detection, assessment, understanding and prevention of adverse effects or any other drug-related problems</p>
  <a href="#">Read more...</a>
</div>
<div class="abs info" style="left:148px;top:1151px">
  <h3>Our primary functions</h3>
  <p>Our primary functions are EU QPPV and related pharmacovigilance services to assist and support Marketing Authorisation Holders (MAH), of pharmaceutical product</p>
  <a href="#">Read more...</a>
</div>
<div class="abs info" style="left:659px;top:1151px">
  <h3>Good Pharmacovigilance Practice</h3>
  <p>is dependant on a sound understanding of the key principles of this science and the ability to apply this knowledge competently on behalf of the client.</p>
  <a href="#">Read more...</a>
</div>

<h2 class="abs section-title" style="top:1390px">Our Services</h2>

<div class="abs card" style="left:203px;top:1482px">
  <svg width="34" height="32" viewBox="0 0 34 32" fill="none" stroke="#333" stroke-width="1.4"><path d="M18 12c-4-3-7-5-7-8a3 3 0 0 1 7-1 3 3 0 0 1 7 1c0 3-3 5-7 8z"/><path d="M3 20h6l6 2h6a2 2 0 0 1 0 4h-7M9 28l8 2 14-7a2 2 0 0 0-2-3l-7 3M3 18v12"/></svg>
  <h4>Medical Information</h4>
  <p>Professional enquiry handling to support the safe and effective use of your products.</p>
  <a class="btn" href="#">Get started</a>
</div>
<div class="abs card" style="left:718px;top:1482px">
  <svg width="34" height="32" viewBox="0 0 34 32" fill="none" stroke="#333" stroke-width="1.6"><path d="M17 29C7 21 2 16 2 10a7 7 0 0 1 15-3 7 7 0 0 1 15 3c0 6-5 11-15 19z"/><path d="M5 15h7l2-4 4 8 2-4h9"/></svg>
  <h4>Pharmacovigilance</h4>
  <p>Ease the regulatory burden and keep compliant with current pharmacovigilance.</p>
  <a class="btn" href="#">Get started</a>
</div>
<div class="abs card" style="left:202px;top:1835px">
  <svg width="38" height="36" viewBox="0 0 38 36" fill="none" stroke="#333" stroke-width="1.4"><rect x="2" y="2" width="26" height="22"/><path d="M6 18l6-6 5 4 7-9"/><circle cx="24" cy="24" r="7"/><path d="M29 29l6 6"/></svg>
  <h4>Literature Monitoring</h4>
  <p>Product safety through surveillance of published articles and case reports.</p>
  <a class="btn" href="#">Get started</a>
</div>
<div class="abs card" style="left:718px;top:1837px">
  <svg width="36" height="34" viewBox="0 0 36 34" fill="none" stroke="#333" stroke-width="1.4"><rect x="2" y="2" width="32" height="22"/><path d="M12 30h12M18 24v6M10 12l8-4 8 4-8 4z M13 14v4c3 2 7 2 10 0v-4"/></svg>
  <h4>Training</h4>
  <p>Professional enquiry handling to support the safe and effective use of your products.</p>
  <a class="btn" href="#">Get started</a>
</div>

<footer class="abs footer">
  <h2 style="left:207px;top:72px">Contacts</h2>
  <p style="left:207px;top:146px">Contact us on 020 7946 0183</p>
  <div class="social"><span></span><span></span><span></span><span></span></div>
  <h2 style="left:796px;top:72px">Link to our</h2>
  <p style="left:797px;top:146px">SAFEWATCH platform</p>
  <div class="abs brand" style="left:318px;top:347px"><span class="brand-mark"></span>Quorvanta</div>
  <div class="abs copy">Copyright © 2020 Quorvanta Ltd<br>(Registered in England &amp; Wales: 04418260)</div>
</footer>

</body>
</html>
```